indoor tennis and sports center( club)

we need a logo for a new business venture, it will be for business cards and for presentations.
presentations for potential investors and authorities.
the design needs to communicate the sport and a community of tennis players
the center includes a tennis academy, and sports club with training sessions for all ages

Project Deadline Extended
Reason: so that I can get some more feedback on my side as to te design we want

Target Market(s)

potential investors or partners

Industry/Entity Type

Business

Contact Information for Business Card

i need the name of the club
names of the partners
slogan" changing lives through tennis" on the front
the clubs three main goals are ports education , academy and a community club

Colors
3176b5
33b8a4
fbee3d
0dac94
acd036

Requirements
Must have
• a strong logo
• names of the partners
• web site and email address
• tel number
Nice to have
• a connection between the different aspects of the club

```html
<!DOCTYPE html>
<html lang="en">
<head>
<meta charset="UTF-8">
<title>Baseline Hall – Business Cards</title>
<link href="https://fonts.googleapis.com/css2?family=Open+Sans:wght@400;600;700&family=Libre+Baskerville&display=swap" rel="stylesheet">
<style>
  :root {
    --teal: #0dac94;
    --teal-light: #33b8a4;
    --lime: #acd036;
    --yellow: #fbee3d;
    --blue: #3176b5;
    --white: #ffffff;
    --ink: #1b1b1b;
    --backdrop: #e4e5e7;
  }
  * { box-sizing: border-box; margin: 0; padding: 0; }
  html, body {
    width: 1200px; height: 800px; overflow: hidden;
    background: var(--backdrop);
    font-family: "Open Sans", Arial, sans-serif;
  }
  .canvas { position: relative; width: 1200px; height: 800px; }
  .card {
    position: absolute; width: 520px; height: 297px;
    background: var(--white); overflow: hidden;
    box-shadow: 0 6px 18px rgba(0,0,0,0.12);
  }

  /* Goals card */
  .goals-card { left: 50px; top: 250px; background: var(--teal); }
  .goals-card .brand {
    position: absolute; top: 62px; left: 0; width: 100%;
    display: flex; justify-content: center; align-items: center; gap: 14px;
  }
  .brand-dot {
    width: 46px; height: 46px; border-radius: 50%;
    background: var(--lime); border: 3px solid var(--yellow);
  }
  .goals-card .brand-name {
    font-weight: 700; font-size: 30px; letter-spacing: 1px; color: var(--white);
  }
  .goals-title {
    position: absolute; top: 138px; width: 100%; text-align: center;
    font-family: "Libre Baskerville", Georgia, serif;
    font-size: 22px; color: #d6f08a;
  }
  .goals-band {
    position: absolute; left: 0; bottom: 0; width: 100%; height: 82px;
    background: var(--white);
    display: flex; align-items: center; justify-content: center; gap: 14px;
    font-size: 19px; color: var(--ink);
  }

  /* Contact card */
  .contact-card { left: 630px; top: 250px; }
  .contact-card .wave { position: absolute; inset: 0; }
  .contact-card .brand {
    position: absolute; top: 26px; left: 28px;
    display: flex; align-items: center; gap: 14px;
  }
  .contact-card .brand-dot { width: 40px; height: 40px; }
  .brand-rule { width: 2px; height: 54px; background: var(--teal); }
  .contact-card .brand-name {
    font-weight: 700; font-size: 15px; color: var(--ink); letter-spacing: 0.5px;
  }
  .slogan { font-size: 13px; line-height: 1.25; color: var(--ink); margin-top: 3px; }
  .contact {
    position: absolute; right: 28px; top: 152px;
    color: var(--white); font-size: 12.5px; line-height: 1.35;
  }
  .contact .person { font-size: 24px; font-weight: 400; line-height: 1.1; }
  .contact .role { margin-bottom: 4px; }
</style>
</head>
<body>
<main class="canvas">

  <section class="card goals-card">
    <div class="brand">
      <span class="brand-dot"></span>
      <span class="brand-name">BASELINE HALL</span>
    </div>
    <h2 class="goals-title">Our Main Goals</h2>
    <div class="goals-band">
      <span>Ports Education</span><span>/</span>
      <span>Academy</span><span>/</span>
      <span>Community Club</span>
    </div>
  </section>

  <section class="card contact-card">
    <svg class="wave" viewBox="0 0 520 297" width="520" height="297" aria-hidden="true">
      <path d="M0 78 C110 160 230 140 340 142 C430 144 490 170 520 196 V297 H0 Z" fill="var(--teal)"/>
    </svg>
    <div class="brand">
      <span class="brand-dot"></span>
      <span class="brand-rule"></span>
      <div>
        <div class="brand-name">BASELINE HALL</div>
        <p class="slogan">Changing Lives<br>Through Tennis</p>
      </div>
    </div>
    <address class="contact" style="font-style:normal">
      <div class="person">Sam Rivera</div>
      <div class="role">Manager</div>
      <div>#4321, 88 Court Lane, Rivertown</div>
      <div>Lakeside, USA 10254</div>
      <div>www.baselinehall.com</div>
      <div>team@baselinehall.com</div>
      <div>1-800-555-RALLY (#456)</div>
    </address>
  </section>

</main>
</body>
</html>
```